Commercial/Corporate Law Firm needs Website Design

Hi guys. I've started up a new law firm and would love your help designing an attractive website. I'll need both design and coding, and to make it easy for us to edit as necessary later, I think it should be built off a Wordpress.org structure.
FIRST IMPRESSIONS
It's very important that the first impression of the website really captures our prospective clients' attention and impresses them. Their first three seconds needs to be good.
I imagine the homepage may be short, with a menu bar and a compelling image, and with a tagline overlaid or underneath (eg. "It's about results.")
The image should be related to our practice areas: eg. IPOs, corporate transactions, or commercial negotiations.
I have previously suggested there could be a skyline image of Harbour City or Adelaide. However, because we are based in Adelaide, I don't think Harbour City is appropriate - and Adelaide is probably too boring to use.
HOMEPAGE
Being a new firm, we don't have many existing testimonials, and I will be the only lawyer to start with. So we need to focus on the nature of the services we will provide and how my experience can help them. We have an existing logo to use, and I would like the website colour scheme not to clash with that logo (dark blue and white).
After the initial image and tagline there should be a brief introduction to each of the main areas of work, eg. "We specialise in three main areas of practice:"
1. Corporate Transactions and Regulation
2. Business Law and Dispute Resolution
3. Migration Assistance
These should each have an appropriate photo and link to a separate page that briefly describes our services in that area.
Below that there should be a message from me with a photo. Finally, at the bottom, there should be a "Contact Us" section which shows a Google image of our address, contact details, and then our logo with colours inverted.
OTHER PAGES
While we will need some other pages, they should all be fairly simple. I think we will need one page to say "About Us", where I will put information about my experience. I think we will then need one page for each of the 3 areas listed above, which just needs an appropriate image and then text to describe the service. Finally, a "Contact Us" page which I imagine will be the same as the bottom of the homepage.
OTHER DETAILS
For now you can use details from my LinkedIn page to fill out any other text as necessary, or the photo.
Because the logo is square, I would prefer the design of the website also to be rectangular.
Looking forward to seeing your work! Thank you.
Good luck,
Marcus
Target Market(s)
Potential clients:
Businesses with legal issues or disputes
Companies wishing to list on the stock market

```html
<!DOCTYPE html>
<html lang="en">
<head>
<meta charset="utf-8">
<title>Corvell Legal — It's About Results</title>
<link href="https://fonts.googleapis.com/css2?family=Roboto:wght@400;500;700;900&family=Open+Sans:wght@400;600&display=swap" rel="stylesheet">
<style>
:root{
  --navy:#1c355e;
  --navy-dark:#152a4c;
  --sky:#3ea3dc;
  --ink:#1f2a3c;
  --muted:#8a8f99;
  --map:#2c2c2c;
  --line:#d6d9de;
  --white:#ffffff;
  --bar:#3a2a26;
}
*{box-sizing:border-box;margin:0;padding:0}
html,body{width:1200px;height:3209px;overflow:hidden}
body{position:relative;background:var(--white);font-family:"Open Sans",Arial,sans-serif;color:var(--ink)}
.abs{position:absolute}
svg.band{position:absolute;left:0;display:block}

/* hero */
.hero-bg{top:0;height:524px;width:1200px}
.brand{top:14px;left:257px;display:flex;align-items:center;gap:10px;color:var(--white);font-family:"Roboto",Arial,sans-serif;font-weight:700;font-size:17px;letter-spacing:2px;white-space:nowrap}
.brand .mark{width:22px;height:22px;background:var(--white)}
.nav{top:30px;left:478px;display:flex;font-family:"Roboto",Arial,sans-serif;font-size:11px;font-weight:500;color:var(--white);letter-spacing:.5px}
.nav a{color:inherit;text-decoration:none;width:86px;text-align:center;padding-bottom:6px}
.nav a.active{color:var(--sky);border-bottom:2px solid var(--white);width:58px;margin:0 14px}
.cta-top{top:28px;left:828px;width:115px;height:25px;border-radius:13px;background:var(--navy);color:var(--white);font:500 10px "Roboto",Arial,sans-serif;display:flex;align-items:center;justify-content:center;white-space:nowrap}
.hero-kicker{top:209px;left:257px;color:var(--white);font:500 14px "Roboto",Arial,sans-serif;letter-spacing:.5px}
.hero-title{top:226px;left:255px;color:var(--white);font:700 38px "Roboto",Arial,sans-serif;letter-spacing:1px;white-space:nowrap}
.hero-tag{top:266px;left:257px;color:var(--sky);font:700 21px "Roboto",Arial,sans-serif;letter-spacing:1px}
.hero-copy{top:300px;left:257px;width:340px;color:#d7dbe2;font-size:10px;line-height:14px}
.btn{display:flex;align-items:center;justify-content:center;border-radius:14px;font:500 10px "Roboto",Arial,sans-serif;color:var(--white);letter-spacing:.5px;white-space:nowrap}
.btn-solid{background:var(--navy)}
.btn-ghost{border:1px solid var(--white)}

/* about */
.eyebrow{font:500 9px "Roboto",Arial,sans-serif;color:var(--muted);letter-spacing:.5px}
.about-title{top:652px;left:263px;font:700 26px/30px "Roboto",Arial,sans-serif;color:var(--navy);white-space:nowrap}
.about-title span{color:var(--sky)}
.about-copy{top:652px;left:554px;width:380px;font-size:12px;line-height:19px;color:var(--muted)}

/* services */
.svc-head{top:975px;width:1200px;text-align:center;color:var(--white)}
.svc-head .eyebrow{color:#c8d0dc}
.svc-head h2{font:700 40px "Roboto",Arial,sans-serif;margin-top:2px}
.grid{top:1070px;left:244px;width:712px;height:357px;display:grid;grid-template-columns:repeat(3,1fr);grid-template-rows:repeat(2,1fr)}
.tile-photo{width:100%;height:100%}
.tile-text{color:var(--white);text-align:center;padding:40px 22px 0;display:flex;flex-direction:column;align-items:center;justify-content:center}
.tile-text h3{font:700 15px/17px "Roboto",Arial,sans-serif;margin-bottom:14px}
.tile-text p{font-size:10px;line-height:15px;color:#b4bfcf}
.see-all{top:1491px;left:535px;width:130px;height:24px;border:1px solid var(--white);border-radius:12px;color:var(--white);font:500 9px "Roboto",Arial,sans-serif;display:flex;align-items:center;justify-content:center;white-space:nowrap}

/* message */
.portrait{top:1784px;left:244px;width:355px;height:334px;background:linear-gradient(160deg,#1b2233 0%,#2f3b56 45%,#6b5a4a 100%);box-shadow:0 6px 14px rgba(0,0,0,.25)}
.quote-mark{top:1858px;left:631px;font:900 40px "Roboto",Arial,sans-serif;color:#b8bcc4}
.quote{top:1906px;left:631px;width:345px;font-size:10px;line-height:18px;color:var(--ink)}
.quote-name{top:2008px;left:631px;font:700 20px "Roboto",Arial,sans-serif;color:var(--navy)}
.quote-role{top:2034px;left:631px;font-size:10px;color:#c3c7ce;letter-spacing:1px}

/* contact */
.contact-title{top:2712px;left:250px;font:700 38px "Roboto",Arial,sans-serif;color:var(--navy)}
.field{left:250px;width:343px;border:1px solid var(--line);font-size:9px;color:var(--muted);padding:5px 7px}
.send{top:2900px;left:250px;width:343px;height:22px;background:var(--navy);color:var(--white);font:500 10px "Roboto",Arial,sans-serif;display:flex;align-items:center;justify-content:center}
.col-title{font:700 11px "Roboto",Arial,sans-serif;color:var(--ink)}
.col-line{font-size:10px;line-height:17px;color:#b0b4bb;white-space:nowrap}
.social{top:2871px;left:785px;display:flex;gap:8px}
.social span{width:26px;height:26px;background:#eef0f3;border:1px solid var(--line)}

/* footer */
.footer{top:3044px;left:0;width:1200px;height:149px;background:var(--navy)}
.footer-brand{top:3080px;left:296px;width:100px;color:var(--white);font:700 12px/14px "Roboto",Arial,sans-serif;letter-spacing:2px;display:flex;flex-direction:column;align-items:center;gap:6px;text-align:center}
.footer-brand .mark{width:18px;height:18px;background:var(--white)}
.f-title{font:700 10px "Roboto",Arial,sans-serif;color:var(--white)}
.f-text{font-size:8px;line-height:12px;color:#a9b5c8}
.f-links{font:500 8px/15px "Roboto",Arial,sans-serif;color:var(--white)}
.f-input{top:3108px;left:731px;width:163px;height:23px;background:var(--white);border-radius:12px 0 0 12px;font-size:8px;color:var(--muted);padding:6px 10px}
.f-send{top:3108px;left:894px;width:47px;height:23px;background:#8d96a4;border-radius:0 12px 12px 0;color:var(--white);font:500 9px "Roboto",Arial,sans-serif;display:flex;align-items:center;justify-content:center}
.bottom-bar{top:3193px;left:0;width:1200px;height:16px;background:var(--bar);color:#e7d9d2;font-size:7px;text-align:center;line-height:16px}
</style>
</head>
<body>

<!-- hero -->
<svg class="band hero-bg" width="1200" height="524" viewBox="0 0 1200 524" role="img" aria-label="Photo of a business handshake over a desk with laptop and documents">
  <defs>
    <linearGradient id="heroFill" x1="0" y1="0" x2="1" y2="1">
      <stop offset="0" stop-color="#2a211c"/>
      <stop offset=".5" stop-color="#3d322b"/>
      <stop offset="1" stop-color="#1d1a1a"/>
    </linearGradient>
  </defs>
  <polygon points="0,0 1200,0 1200,417 0,524" fill="url(#heroFill)"/>
</svg>

<div class="abs brand"><span class="mark"></span>CORVELL LEGAL</div>
<nav class="abs nav">
  <a class="active">HOME</a><a>ABOUT</a><a>SERVICES</a><a>CONTACT</a>
</nav>
<div class="abs cta-top">GET STARTED NOW!</div>

<div class="abs hero-kicker">WELCOME TO</div>
<h1 class="abs hero-title">CORVELL LEGAL</h1>
<div class="abs hero-tag">IT'S ABOUT RESULTS.</div>
<p class="abs hero-copy">Lorem ipsum dolor sit amet, sed do eiusmod tempor incididunt ut labore et dolore magna aliqua. Mauris mollis consectetur elit, tellus nec ullamcorper mattis sed rutrum. Donec eget lacus.</p>
<div class="abs btn btn-solid" style="top:366px;left:257px;width:92px;height:26px">LEARN MORE</div>
<div class="abs btn btn-ghost" style="top:366px;left:357px;width:88px;height:26px">CONTACT US</div>

<!-- about -->
<div class="abs eyebrow" style="top:626px;left:263px">Learn More About</div>
<h2 class="abs about-title">CORVELL LEGAL<br><span>WE GET RESULTS.</span></h2>
<div class="abs btn btn-solid" style="top:717px;left:263px;width:90px;height:25px">ABOUT US</div>
<p class="abs about-copy">Lorem ipsum dolor sit amet conse ctetur adipiscing elit, sed do eiusmod tempor incididunt ut labore et dolore magna aliqua. Ut enim ad minim veniam, quis nostrud exercitation ullamco laboris nisi ut aliquip ex ea commodo consequat. Lorem ipsum dolor sit amet conse ctetur adipiscing elit, sed do eiusmod tempor incididunt.</p>

<!-- services band -->
<svg class="band" style="top:828px" width="1200" height="872" viewBox="0 0 1200 872">
  <polygon points="0,113 1200,0 1200,766 0,872" fill="var(--navy)"/>
</svg>
<div class="abs svc-head">
  <div class="eyebrow">Learn More About</div>
  <h2>Services</h2>
</div>
<div class="abs grid">
  <div class="tile-photo" role="img" aria-label="Photo of colleagues reviewing charts at a desk" style="background:linear-gradient(135deg,#e9eef3,#9fb2c4 60%,#5d6f86)"></div>
  <div class="tile-text"><h3>Business Law and Dispute Resolution</h3><p>I am text block. Click edit button to change this text. Lorem ipsum dolor sit amet, consectetur adipiscing elit.</p></div>
  <div class="tile-photo" role="img" aria-label="Photo of a passport resting on visa application forms" style="background:linear-gradient(135deg,#dcdfe3,#b9bfc6 55%,#2a2f3d)"></div>
  <div class="tile-text"><h3>Corporate Transactions and Regulation</h3><p>I am text block. Click edit button to change this text. Lorem ipsum dolor sit amet, consectetur adipiscing elit.</p></div>
  <div class="tile-photo" role="img" aria-label="Photo of a hand signing a contract" style="background:linear-gradient(160deg,#3a2b1f,#5a4735 50%,#d9d6d0)"></div>
  <div class="tile-text"><h3>Migration Assistance</h3><p>I am text block. Click edit button to change this text. Lorem ipsum dolor sit amet, consectetur adipiscing elit.</p></div>
</div>
<div class="abs see-all">SEE ALL OUR SERVICES</div>

<!-- message -->
<div class="abs portrait" role="img" aria-label="Portrait of Marcus Whitlow in a suit with a night city skyline behind"></div>
<div class="abs quote-mark">&ldquo;</div>
<p class="abs quote">I am text block. Click edit button to change this text. Lorem ipsum dolor sit amet, consectetur adipiscing elit. Ut elit tellus, luctus nec ullamcorper mattis, pulvinar dapibus leo. It is a long established fact that a reader will be distracted by the readable content of a page when looking at its layout.</p>
<div class="abs quote-name">Marcus Whitlow</div>
<div class="abs quote-role">CORVELL LEGAL FOUNDER</div>

<!-- map -->
<svg class="band" style="top:2175px" width="1200" height="477" viewBox="0 0 1200 477" role="img" aria-label="Dark street map showing the office location in Harbour City">
  <polygon points="0,110 1200,0 1200,381 0,477" fill="var(--map)"/>
  <path d="M600 235c-7 0-12 5-12 12 0 9 12 22 12 22s12-13 12-22c0-7-5-12-12-12z" fill="#e0463b"/>
  <circle cx="600" cy="247" r="4" fill="#7a1f18"/>
</svg>

<!-- contact -->
<h2 class="abs contact-title">Get in touch</h2>
<div class="abs field" style="top:2772px;height:22px">Name</div>
<div class="abs field" style="top:2802px;height:22px">Email</div>
<div class="abs field" style="top:2834px;height:58px">Message</div>
<div class="abs send">Send</div>

<div class="abs col-title" style="top:2780px;left:612px">LOCATION</div>
<div class="abs col-line" style="top:2801px;left:612px">48 Harlow Lane<br>Eastvale, SA 5099</div>
<div class="abs col-title" style="top:2844px;left:612px">OUR HOURS</div>
<div class="abs col-line" style="top:2865px;left:612px">MON-FRI 09:00 - 17:00<br>SAT-SUN 10:00 - 14:00</div>

<div class="abs col-title" style="top:2780px;left:785px">CONTACT US</div>
<div class="abs col-line" style="top:2801px;left:785px">Phone: +61 (08) 7010 4422<br>Email: hello@corvell-legal.example</div>
<div class="abs col-title" style="top:2844px;left:785px">FOLLOW US</div>
<div class="abs social"><span></span><span></span><span></span><span></span></div>

<!-- footer -->
<div class="abs footer"></div>
<div class="abs footer-brand"><span class="mark"></span>CORVELL<br>LEGAL</div>
<div class="abs f-title" style="top:3076px;left:432px">About Us</div>
<p class="abs f-text" style="top:3094px;left:432px;width:150px">I am text block. Click edit button to change this text. Lorem ipsum dolor sit amet, consectetur adipiscing elit. Ut elit tellus, luctus nec ullamcorper mattis, pulvinar dapibus leo.</p>
<div class="abs f-title" style="top:3076px;left:607px">Useful Links</div>
<div class="abs f-links" style="top:3096px;left:607px">HOME<br>ABOUT<br>SERVICES<br>CONTACT</div>
<div class="abs f-title" style="top:3076px;left:731px">Subscribe To Our Newsletter</div>
<div class="abs f-text" style="top:3091px;left:731px">Lorem ipsum dolor. Click edit button to change this text.</div>
<div class="abs f-input">Email</div>
<div class="abs f-send">Send</div>
<div class="abs bottom-bar">Copyright © 2018 Corvell Legal. All Rights Reserved.</div>

</body>
</html>
```